Easter & Summer School Dance Camps

I need two flyers one for Easter camps and one for summer school
We are a performing arts and dance academy

I want a double sided flyers one side summer school one side easter camp

Please make these flyers appeal to young dancers and performers - eye catching up to date Added Tuesday, March 1, 2016

Target Market(s)

Young children and teenagers

Industry/Entity Type

School

Font styles to use
Serif
Sans Serif

Requirements
Must have
• bright colourful

```html
<!DOCTYPE html>
<html lang="en">
<head>
<meta charset="utf-8">
<title>Easter Workshops – Brightstep Academy</title>
<link href="https://fonts.googleapis.com/css2?family=Yellowtail&family=Kaushan+Script&family=Caveat:wght@400;500&family=Kalam:wght@700&display=swap" rel="stylesheet">
<style>
  :root {
    --page: #ffffff;
    --blush: #f8d3e0;
    --hot-pink: #e8559a;
    --title-pink: #e2468a;
    --mauve: #a8436a;
    --ink: #1a1a1a;
    --white: #ffffff;
    --hero-light: #fbeeb8;
  }
  * { box-sizing: border-box; margin: 0; padding: 0; }
  html, body { width: 925px; height: 1200px; overflow: hidden; background: var(--page); }
  .canvas { position: relative; width: 925px; height: 1200px; }
  .flyer {
    position: absolute; left: 108px; top: 100px; width: 709px; height: 1000px;
    background: var(--blush); overflow: hidden;
  }
  .abs { position: absolute; white-space: nowrap; }

  .hero-art {
    position: absolute; left: 100px; top: 40px; width: 500px; height: 360px;
    border-radius: 40px;
    background: radial-gradient(ellipse at 50% 45%, var(--hero-light) 0%, #f3c9a8 45%, rgba(168,71,95,0.35) 80%, rgba(248,211,224,0) 100%);
  }

  .script-title {
    font-family: "Yellowtail", "Kaushan Script", cursive; font-weight: 400; color: var(--title-pink);
    line-height: 1.1;
    text-shadow: 2px 2px 0 var(--white), -2px -2px 0 var(--white), 2px -2px 0 var(--white), -2px 2px 0 var(--white), 0 3px 4px rgba(120,40,70,0.35);
    transform: translateX(-50%);
  }
  .easter-title { left: 352px; top: 400px; font-size: 50px; }
  .westend-title { left: 354px; top: 700px; font-size: 56px; }

  .copy {
    font-family: "Caveat", cursive; color: var(--mauve); font-size: 22px; line-height: 1;
  }
  .copy.centered { left: 0; width: 709px; text-align: center; }

  .band { position: absolute; background: var(--hot-pink); }
  .band-text {
    font-family: "Kaushan Script", cursive; color: var(--white); line-height: 1;
  }

  .small-copy { font-family: "Caveat", cursive; color: var(--mauve); font-size: 16px; }
  .detail-copy { font-family: "Caveat", cursive; color: var(--mauve); font-size: 19px; }

  .label { font-family: "Caveat", cursive; color: var(--white); font-size: 16px; line-height: 1; }
  .fine {
    font-family: "Kalam", cursive; font-weight: 700; color: var(--ink); font-size: 11.5px;
  }

  .logo-arch { position: absolute; left: 402px; top: 780px; width: 307px; height: 220px; }
  .brand {
    position: absolute; left: 420px; top: 888px; width: 260px; text-align: center;
    font-family: "Caveat", cursive; font-weight: 500; color: var(--ink);
  }
  .brand-name { display: block; font-size: 52px; line-height: 1; }
  .brand-line { display: block; font-size: 11px; line-height: 1.1; margin-top: 12px; white-space: nowrap; }
  .brand-mark {
    position: absolute; left: 448px; top: 872px; width: 14px; height: 14px;
    background: var(--hot-pink); border-radius: 50%;
  }
</style>
</head>
<body>
<div class="canvas">
  <div class="flyer">

    <div class="hero-art" role="img" aria-label="Bubble-lettered title “Once Upon a Time” with silhouettes of dancing children and stars"></div>

    <h1 class="abs script-title easter-title">Easter Workshops</h1>

    <p class="abs copy centered" style="top:454px;">This spring, your child will enjoy a joyous journey to</p>
    <p class="abs copy centered" style="top:481px;">the magical world of Once Upon a Time for a fabulous springtime treat.</p>
    <p class="abs copy centered" style="top:523px;">We will work our magic to ensure your child enjoys every minute.</p>
    <p class="abs copy centered" style="top:550px;">Guiding each child every step of the way and inspire and encourage them</p>
    <p class="abs copy centered" style="top:578px;">to project their voices, learn energetic dance routines, sing catchy songs,</p>
    <p class="abs copy centered" style="top:605px;">and more importantly HAVE FUN!</p>

    <div class="band" style="left:167px; top:631px; width:393px; height:24px; transform:rotate(-0.6deg);"></div>
    <p class="abs band-text" style="left:247px; top:633px; font-size:20px;">Tuesday 5 &amp; 6 April 2016</p>

    <p class="abs small-copy" style="left:174px; top:670px;">Age 3 – 7 years 10 – 12pm 18 per day&nbsp; or 30 for both days</p>

    <h2 class="abs script-title westend-title">West End Workshop</h2>

    <svg class="logo-arch" viewBox="0 0 307 220" aria-hidden="true">
      <path d="M0,220 L0,130 C0,50 70,0 150,0 C230,0 280,60 280,130 L280,220 Z" fill="#ffffff"/>
    </svg>

    <div class="band" style="left:10px; top:846px; width:394px; height:32px; transform:rotate(1.4deg);"></div>
    <p class="abs band-text" style="left:90px; top:852px; font-size:22px; transform:rotate(1.4deg);">Tuesday 5 &amp; 6 April 2016</p>

    <p class="abs copy" style="left:64px; top:780px;">Our Easter dance camps are fun, fresh and</p>
    <p class="abs copy" style="left:112px; top:803px;">funky, mixed together with</p>
    <p class="abs copy" style="left:202px; top:825px;">a little musical theatre!</p>

    <p class="abs detail-copy" style="left:78px; top:884px;">8 – 16 years, 1-4pm 30 per day/ 55 for both</p>

    <div class="band" style="left:0; top:913px; width:132px; height:13px;"></div>
    <p class="abs label" style="left:64px; top:910px;">venue</p>
    <p class="abs fine" style="left:58px; top:930px;">The Parish Hall of St Aldric Millbrook KT9 4ZZ</p>

    <div class="band" style="left:300px; top:947px; width:102px; height:13px;"></div>
    <p class="abs label" style="left:304px; top:944px;">contact us</p>
    <p class="abs fine" style="left:58px; top:966px;">brightstepdance@mailbox.example to book or Text 07700 900418</p>

    <span class="brand-mark" aria-hidden="true"></span>
    <div class="brand">
      <span class="brand-name">brightstep</span>
      <span class="brand-line">ACADEMY OF DANCE AND PERFORMING ARTS</span>
    </div>

  </div>
</div>
</body>
</html>
```